Direct Mail flyer for the timeshare industry.

We need someone who has experience in direct mail experience in postcards and successful campaigns. The post card we are using is not good at all.

We are looking at a 5.5 x 8.5 postcard with 4 color on one side and the black and white on the mailing side. But if someone has a better idea instead of a postcard then I am open to that

Target Market(s)

Timeshare owners...most of them are 55 plus in age. We help people get out of their time share

Industry/Entity Type

Industry

Font styles to use
Serif

Colors

Designer to choose colors to be used in the design.

Requirements
Must have
• Call to action and be easy to understand and look very professional and not fake or cheesy

```html
<!DOCTYPE html>
<html lang="en">
<head>
<meta charset="utf-8">
<title>Harbor Point Group – Private Event Invitation Postcard</title>
<link rel="stylesheet" href="https://fonts.googleapis.com/css2?family=Oswald:wght@300;400;500;600;700&display=swap">
<style>
  :root {
    --backdrop: #2a2a2a;
    --navy-deep: #050c24;
    --navy: #0b1d4a;
    --navy-light: #1b3c7e;
    --glow: #8fc2ff;
    --red: #e0252b;
    --red-dark: #a5121a;
    --white: #ffffff;
    --text-soft: #dfe6f3;
    --mail-text: #6f7175;
    --rule: #c9cbcd;
    --stamp: #eceeee;
  }
  * { box-sizing: border-box; margin: 0; padding: 0; }
  html, body { width: 960px; height: 1200px; overflow: hidden; }
  body {
    background: var(--backdrop);
    font-family: "Oswald", sans-serif;
    position: relative;
  }

  .card { position: absolute; left: 80px; width: 802px; height: 519px; overflow: hidden; }

  /* ---------- Front ---------- */
  .card--front {
    top: 77px;
    background:
      linear-gradient(90deg, transparent 83%, rgba(80,150,255,.18) 84%, transparent 86%),
      linear-gradient(90deg, transparent 66%, rgba(80,150,255,.12) 67%, transparent 68%),
      radial-gradient(ellipse at 70% 30%, var(--navy-light) 0%, var(--navy) 40%, var(--navy-deep) 100%);
    color: var(--white);
  }
  .front__art {
    position: absolute; left: -40px; right: -40px; top: 375px; height: 320px;
    border-radius: 50% 50% 0 0 / 60% 60% 0 0;
    background: radial-gradient(ellipse at 45% 20%, #e9f1fb 0%, #a9c4e4 30%, #4c76b4 60%, rgba(20,50,110,0) 85%);
    opacity: .85;
  }
  .eyebrow {
    position: absolute; left: 32px; top: 36px;
    font-weight: 400; font-size: 29px; line-height: 35px; letter-spacing: .2px;
    text-transform: uppercase;
  }
  .headline {
    position: absolute; left: 218px; top: 24px;
    font-weight: 600; font-size: 76px; line-height: 84px; color: var(--red);
    letter-spacing: -1px; transform: scaleX(.86); transform-origin: left;
  }
  .intro {
    position: absolute; left: 32px; top: 116px;
    font-weight: 300; font-size: 26px; line-height: 33px; color: var(--text-soft);
  }
  .intro__free { display: block; color: var(--red); font-weight: 600; letter-spacing: .3px; }
  .schedule {
    position: absolute; left: 32px; top: 230px;
    display: flex; align-items: center; gap: 8px;
    font-size: 23px; font-weight: 400;
  }
  .schedule__times { font-size: 17px; margin-left: 8px; }
  .cta { position: absolute; left: 31px; top: 278px; }
  .cta__label { font-weight: 300; font-size: 38px; line-height: 44px; }
  .cta__phone { font-weight: 600; font-size: 38px; line-height: 44px; color: var(--red); }
  .divider { position: absolute; left: 278px; top: 280px; width: 2px; height: 82px; background: var(--white); opacity: .8; }
  .venue { position: absolute; left: 302px; top: 285px; }
  .venue__pin { position: absolute; left: 0; top: 2px; }
  .venue__name { margin-left: 22px; font-size: 19px; font-weight: 300; line-height: 24px; }
  .venue__address { margin-left: 22px; font-size: 26px; font-weight: 300; line-height: 30px; }

  .benefits { position: absolute; left: 544px; top: 40px; width: 240px; }
  .benefit { margin-bottom: 24px; }
  .benefit__title {
    display: flex; align-items: center; gap: 12px;
    font-weight: 600; font-size: 22px; line-height: 30px; letter-spacing: .3px;
  }
  .benefit__text { font-weight: 300; font-size: 14px; line-height: 17px; color: var(--text-soft); margin-top: 6px; }

  .rsvp {
    position: absolute; left: 202px; top: 459px; width: 398px; height: 42px;
    border-radius: 21px; background: linear-gradient(180deg, var(--red), var(--red-dark));
    display: flex; align-items: center; justify-content: center;
    font-size: 29px; font-weight: 500; letter-spacing: .3px;
  }

  /* ---------- Mailing side ---------- */
  .card--back { top: 626px; background: var(--white); }
  .return-address {
    position: absolute; left: 32px; top: 30px;
    font-weight: 300; font-size: 22px; line-height: 31px; color: var(--mail-text);
  }
  .stamp { position: absolute; left: 682px; top: 34px; width: 90px; height: 90px; background: var(--stamp); }
  .address-line { position: absolute; left: 54px; width: 695px; height: 2px; background: var(--rule); }
</style>
</head>
<body>

<section class="card card--front" aria-label="Invitation front">
  <div class="front__art" role="img" aria-label="Glowing globe wrapped in a network of connected points"></div>

  <p class="eyebrow">A Private Event<br>Limited Seating</p>
  <h1 class="headline">INVITATION</h1>

  <p class="intro">This is your chance! We’ve arranged for you and<br>one guest to attend our Harbor Point Group Event
    <span class="intro__free">FREE OF CHARGE</span></p>

  <p class="schedule">
    <svg width="24" height="22" viewBox="0 0 24 22" aria-hidden="true">
      <rect x="1" y="3" width="18" height="16" rx="2" fill="none" stroke="#e0252b" stroke-width="2"/>
      <line x1="1" y1="8" x2="19" y2="8" stroke="#e0252b" stroke-width="2"/>
      <line x1="6" y1="1" x2="6" y2="5" stroke="#e0252b" stroke-width="2"/>
      <line x1="14" y1="1" x2="14" y2="5" stroke="#e0252b" stroke-width="2"/>
      <circle cx="18" cy="16" r="5" fill="#0b1d4a" stroke="#e0252b" stroke-width="2"/>
      <path d="M18 13.5v3h2" stroke="#e0252b" stroke-width="1.5" fill="none"/>
    </svg>
    Saturday, February 17, 2018
    <span class="schedule__times">10:30 AM &nbsp;|&nbsp; 3:00 PM &nbsp;|&nbsp; 6:00 PM</span>
  </p>

  <div class="cta">
    <p class="cta__label">CALL US TODAY</p>
    <p class="cta__phone">(888) 555-0142</p>
  </div>

  <div class="divider"></div>

  <div class="venue">
    <svg class="venue__pin" width="14" height="20" viewBox="0 0 14 20" aria-hidden="true">
      <path d="M7 0a7 7 0 0 1 7 7c0 5-7 13-7 13S0 12 0 7a7 7 0 0 1 7-7z" fill="#e0252b"/>
      <circle cx="7" cy="7" r="2.6" fill="#0b1d4a"/>
    </svg>
    <p class="venue__name">LAKESIDE GARDEN HOTEL</p>
    <p class="venue__address">2150 Meridian Parkway<br>Fort Worth, TX 76137</p>
  </div>

  <div class="benefits">
    <div class="benefit">
      <h2 class="benefit__title">
        <svg width="24" height="20" viewBox="0 0 24 20" aria-hidden="true" fill="none" stroke="#fff" stroke-width="2">
          <path d="M2 4l10-3 10 3-10 3z"/><path d="M2 9l10 3 10-3"/><path d="M2 14l10 3 10-3"/>
        </svg>EDUCATION</h2>
      <p class="benefit__text">We promise this event will be an eye-opening experience and an incredible learning opportunity regardless of your current situation.</p>
    </div>
    <div class="benefit">
      <h2 class="benefit__title">
        <svg width="24" height="24" viewBox="0 0 24 24" aria-hidden="true" fill="#fff">
          <circle cx="12" cy="7" r="4"/>
          <path d="M1 10l6 6v7H4v-5L0 13zM23 10l-6 6v7h3v-5l4-5z"/>
        </svg>PROTECTION</h2>
      <p class="benefit__text">Arm yourself with the knowledge of how to avoid the current scams occurring in the timeshare industry to protect you as an owner.</p>
    </div>
    <div class="benefit">
      <h2 class="benefit__title">
        <svg width="26" height="22" viewBox="0 0 26 22" aria-hidden="true" fill="#fff">
          <circle cx="5" cy="4" r="3"/><circle cx="21" cy="4" r="3"/>
          <rect x="2" y="8" width="6" height="8"/><rect x="18" y="8" width="6" height="8"/>
          <rect x="7" y="11" width="12" height="2"/><rect x="12" y="13" width="2" height="8"/>
        </svg>ADVISEMENT</h2>
      <p class="benefit__text">Your questions are welcomed and will be addressed. This will bring you the sense of confidence that you have been seeking.</p>
    </div>
  </div>

  <p class="rsvp">RSVP Code # HPG70218</p>
</section>

<section class="card card--back" aria-label="Mailing side">
  <address class="return-address" style="font-style:normal">
    Harbor Point Group, LLC<br>
    720 W Maple Ridge Road<br>
    Springfield, Mo. 65810
  </address>
  <div class="stamp"></div>
  <div class="address-line" style="top:220px"></div>
  <div class="address-line" style="top:289px"></div>
  <div class="address-line" style="top:358px"></div>
</section>

</body>
</html>
```